Marwick Agency (http://mk.fennoweb-studio.com/)

We are looking for a similar design to what we have, but more professional looking and cleaned up with links and logo that is not so grainy looking. We are an independent insurance agency marketing to personal and commercial clients. We offer all commercial lines markets and all personal lines. We target excavators, landscapers, restaurants, golf courses, contractors. Please look at http://mk.fennoweb-studio.com/ which we had designed but do not like it, it will give you an idea of what we are looking for.

Target Market(s)

Commercial and personal insurance. All business products and all personal (homeowners, auto, antique auto, umbrella)

Industry/Entity Type

It Professional

Logo Text

Knowledge Building Your Assurance

Number of Pages Required

5+ page

Colors
000000
848484
0255a3

```html
<!DOCTYPE html>
<html lang="en">
<head>
<meta charset="utf-8">
<title>Marwick Agency – Auto Insurance</title>
<link href="https://fonts.googleapis.com/css2?family=Roboto:wght@300;400;500;700&display=swap" rel="stylesheet">
<style>
:root{
  --black:#000;
  --grey:#848484;
  --grey-dark:#6b6b6b;
  --blue:#0255a3;
  --blue-text:#0a5fb4;
  --ink:#222;
  --muted:#444;
  --white:#fff;
  --line:#c9c9c9;
}
*{box-sizing:border-box;margin:0;padding:0}
html,body{width:932px;height:1200px;overflow:hidden}
body{font-family:'Roboto',Arial,sans-serif;color:var(--ink);background:var(--white);position:relative}
a{color:inherit;text-decoration:none}

.site-header{position:absolute;left:0;top:0;width:932px;height:52px;background:var(--black)}
.brand{position:absolute;left:158px;top:14px;display:flex;align-items:center;gap:7px;color:var(--white);font-size:18px;font-weight:500}
.brand-mark{width:22px;height:22px;background:var(--white)}
.top-nav{position:absolute;right:67px;top:0;height:52px;display:flex;align-items:center;gap:22px;font-size:10px;color:var(--white)}

.hero-bg{position:absolute;left:0;top:52px;width:932px;height:303px;background:linear-gradient(180deg,#cfe1f4 0%,#e9f1fa 60%,#f4f8fc 100%)}
.hero-panel{position:absolute;left:123px;top:70px;width:685px;height:285px;background:var(--white)}
.section-nav{height:30px;background:var(--black);display:flex;justify-content:center;align-items:center;font-size:9.5px;color:var(--white)}
.section-nav a{padding:0 8px;border-left:1px solid #777;line-height:12px}
.section-nav a:first-child{border-left:0}
.hero-title{position:absolute;left:28px;top:85px;font-size:30px;font-weight:500;color:var(--blue);letter-spacing:.3px}
.hero-lead{position:absolute;left:28px;top:144px;width:300px;font-size:11.2px;line-height:15px;color:var(--ink)}
.hero-rule{position:absolute;left:28px;top:235px;width:299px;height:1px;background:#aaa}
.faq-link{position:absolute;left:28px;top:248px;font-size:8.5px;color:var(--blue-text)}
.hero-photo{position:absolute;left:350px;top:100px;width:296px;height:138px;border-radius:4px;background:linear-gradient(180deg,#f3f6f9 0%,#7fa3bd 30%,#2f6689 55%,#1d4563 80%,#e9edf0 100%)}

.btn{position:absolute;display:flex;height:26px;background:var(--grey);color:var(--white);font-size:9px;border-radius:2px;overflow:hidden}
.btn-label{flex:1;display:flex;align-items:center;justify-content:center}
.btn-icon{width:27px;background:var(--grey-dark);display:flex;align-items:center;justify-content:center}

.steps-band{position:absolute;left:0;top:355px;width:932px;height:75px;background:var(--blue);color:var(--white)}
.steps-intro{position:absolute;left:151px;top:21px}
.steps-intro h3{font-size:15.5px;font-weight:400}
.steps-intro p{font-size:9.5px;margin-top:1px}
.step{position:absolute;top:24px;display:flex;align-items:center;gap:8px}
.step svg{margin-right:6px}
.step-num{font-size:30px;font-weight:700;line-height:1}
.step-text{font-size:9.5px;line-height:14px}

.feature-photo{position:absolute;width:153px;height:162px}
.feature h3{position:absolute;font-size:17.5px;font-weight:400;line-height:21px;color:var(--ink)}
.feature p{position:absolute;font-size:9.5px;line-height:14.5px;color:var(--muted)}

.tagline{position:absolute;left:0;top:652px;width:932px;text-align:center}
.tagline h2{font-size:18px;font-weight:300;letter-spacing:.4px;color:var(--ink)}
.tagline p{font-size:9.5px;color:var(--muted);margin-top:6px;letter-spacing:.2px}

.card{position:absolute;top:740px;width:153px;height:220px;border:1px solid var(--line);background:var(--white)}
.card-photo{position:absolute;left:3px;top:3px;width:145px;height:139px}
.card h4{position:absolute;left:0;top:156px;width:100%;text-align:center;font-size:12px;font-weight:400;color:var(--blue-text)}

.partners-title{position:absolute;left:0;top:986px;width:932px;text-align:center;font-size:18px;font-weight:300}
.partner{position:absolute;top:1030px;height:28px;background:#c7cdd6;border-radius:3px}

.site-footer{position:absolute;left:0;top:1086px;width:932px;height:114px;background:var(--blue);color:var(--white)}
.footer-nav{position:absolute;left:151px;top:36px;display:flex;gap:20px;font-size:10px;font-weight:500}
.footer-brand{position:absolute;left:661px;top:28px;display:flex;align-items:center;gap:6px;font-size:17px;font-weight:500;color:#b9cde6}
.footer-brand span.mark{width:22px;height:22px;background:#b9cde6}
.footer-rule{position:absolute;left:133px;top:77px;width:665px;height:1px;background:#5c8cc4}
.copyright{position:absolute;left:151px;top:88px;font-size:8.5px}
</style>
</head>
<body>

<header class="site-header">
  <a class="brand" href="#"><span class="brand-mark"></span>Marwick Agency</a>
  <nav class="top-nav">
    <a href="#" aria-label="Home"><svg width="11" height="10" viewBox="0 0 11 10"><path d="M5.5 0 0 5h1.5v5h3V7h2v3h3V5H11z" fill="#2a78c9"/></svg></a>
    <a href="#">About US</a>
    <a href="#">Contact US</a>
  </nav>
</header>

<div class="hero-bg"></div>
<section class="hero-panel">
  <nav class="section-nav">
    <a href="#">Personal Insurance</a><a href="#">Business Insurance</a><a href="#">Auto Insurance</a><a href="#">Home Insurance</a><a href="#">Service Center</a>
  </nav>
  <h1 class="hero-title">Auto Insurance</h1>
  <p class="hero-lead">Temporibus autem quibusdam et aut officiis debitis necessitatibus saepe eveniet ut et voluptates.</p>
  <a class="btn" href="#" style="left:29px;top:186px;width:118px">
    <span class="btn-label">Start Insurance</span>
    <span class="btn-icon"><svg width="10" height="8" viewBox="0 0 10 8"><path d="M1 3V1h7l-1.5-1M9 5v2H2l1.5 1" stroke="#fff" fill="none" stroke-width="1.3"/></svg></span>
  </a>
  <div class="hero-rule"></div>
  <a class="faq-link" href="#">Frequently asked questions</a>
  <div class="hero-photo" role="img" aria-label="Blue SUV car"></div>
</section>

<section class="steps-band">
  <div class="steps-intro"><h3>How it works?</h3><p>do it in just 3 simple steps</p></div>
  <div class="step" style="left:304px">
    <svg width="9" height="16" viewBox="0 0 9 16"><path d="M1 1l7 7-7 7" stroke="#fff" fill="none" stroke-width="1.6"/></svg>
    <span class="step-num">1.</span><span class="step-text">choose an insurance<br>for your needs</span>
  </div>
  <div class="step" style="left:473px">
    <svg width="9" height="16" viewBox="0 0 9 16"><path d="M1 1l7 7-7 7" stroke="#fff" fill="none" stroke-width="1.6"/></svg>
    <span class="step-num">2.</span><span class="step-text">fill a simple form in<br>5 minutes</span>
  </div>
  <div class="step" style="left:645px">
    <svg width="9" height="16" viewBox="0 0 9 16"><path d="M1 1l7 7-7 7" stroke="#fff" fill="none" stroke-width="1.6"/></svg>
    <span class="step-num">3.</span><span class="step-text">pick up the best offer<br>and that's it</span>
  </div>
</section>

<section class="feature">
  <div class="feature-photo" role="img" aria-label="Insurance expert meeting with a client" style="left:133px;top:460px;background:linear-gradient(135deg,#d9dde0,#8a8f94 55%,#3a3d40)"></div>
  <h3 style="left:305px;top:470px">Have a question?<br>Talk to our expert.</h3>
  <p style="left:305px;top:518px;width:150px">Ut aut reiciendis voluptatibus et ores alias consequatur.</p>
  <a class="btn" href="#" style="left:305px;top:555px;width:117px">
    <span class="btn-label">Start Talking</span>
    <span class="btn-icon"><svg width="10" height="9" viewBox="0 0 10 9"><path d="M1 1h8v5H4L2 8V6H1z" fill="#fff"/></svg></span>
  </a>

  <div class="feature-photo" role="img" aria-label="Insurance policy document with glasses and pen" style="left:474px;top:460px;background:linear-gradient(160deg,#c8641e,#e7b07a 50%,#efe6da)"></div>
  <h3 style="left:644px;top:470px">Find the best<br>insurance policy.</h3>
  <p style="left:646px;top:518px;width:160px">Nam libero tempore, cum soluta nobis est eligendi optio cum.</p>
  <a class="btn" href="#" style="left:645px;top:555px;width:118px">
    <span class="btn-label">Find Now</span>
    <span class="btn-icon"><svg width="10" height="10" viewBox="0 0 10 10"><circle cx="4" cy="4" r="3" stroke="#fff" fill="none" stroke-width="1.4"/><path d="M6.2 6.2 9 9" stroke="#fff" stroke-width="1.6"/></svg></span>
  </a>
</section>

<section class="tagline">
  <h2>SMALL ENOUGH TO CARE, BIG ENOUGH TO MAKE A DIFFERENCE</h2>
  <p>Please find information about our agency, its principles , and the various types of insurance coverages that we provide.</p>
</section>

<section class="coverage">
  <article class="card" style="left:133px">
    <div class="card-photo" role="img" aria-label="Yellow excavator on a rocky site" style="background:linear-gradient(180deg,#6f8fb0,#8a7a6a 55%,#e49a1d)"></div>
    <h4>Business Insurance</h4>
    <a class="btn" href="#" style="left:18px;top:181px;width:118px"><span class="btn-label">Get a Quote</span><span class="btn-icon"><svg width="12" height="10" viewBox="0 0 12 10"><path d="M1 1h4v4L3 9H1l2-4H1zM7 1h4v4L9 9H7l2-4H7z" fill="#fff"/></svg></span></a>
  </article>
  <article class="card" style="left:305px">
    <div class="card-photo" role="img" aria-label="Black off-road vehicle" style="background:linear-gradient(180deg,#dcdcdc,#7a7a7a 50%,#1d1d1d)"></div>
    <h4>Auto Insurance</h4>
    <a class="btn" href="#" style="left:18px;top:181px;width:118px"><span class="btn-label">Get a Quote</span><span class="btn-icon"><svg width="12" height="10" viewBox="0 0 12 10"><path d="M1 1h4v4L3 9H1l2-4H1zM7 1h4v4L9 9H7l2-4H7z" fill="#fff"/></svg></span></a>
  </article>
  <article class="card" style="left:475px">
    <div class="card-photo" role="img" aria-label="Grandfather and grandson playing together" style="background:linear-gradient(135deg,#9aa879,#d3b29a 50%,#8a9fb8)"></div>
    <h4>Life Insurance</h4>
    <a class="btn" href="#" style="left:18px;top:181px;width:118px"><span class="btn-label">Get a Quote</span><span class="btn-icon"><svg width="12" height="10" viewBox="0 0 12 10"><path d="M1 1h4v4L3 9H1l2-4H1zM7 1h4v4L9 9H7l2-4H7z" fill="#fff"/></svg></span></a>
  </article>
  <article class="card" style="left:647px">
    <div class="card-photo" role="img" aria-label="Red brick family house with garden" style="background:linear-gradient(180deg,#cfe0ee,#a0563e 45%,#557a3c)"></div>
    <h4>Home Insurance</h4>
    <a class="btn" href="#" style="left:18px;top:181px;width:118px"><span class="btn-label">Get a Quote</span><span class="btn-icon"><svg width="12" height="10" viewBox="0 0 12 10"><path d="M1 1h4v4L3 9H1l2-4H1zM7 1h4v4L9 9H7l2-4H7z" fill="#fff"/></svg></span></a>
  </article>
</section>

<h2 class="partners-title">Our Partners</h2>
<div class="partner" style="left:142px;width:72px"></div>
<div class="partner" style="left:252px;width:84px"></div>
<div class="partner" style="left:381px;width:56px"></div>
<div class="partner" style="left:497px;width:48px"></div>
<div class="partner" style="left:594px;width:84px"></div>
<div class="partner" style="left:715px;width:68px"></div>

<footer class="site-footer">
  <nav class="footer-nav">
    <a href="#">Home</a><a href="#">Our Company</a><a href="#">Insurance</a><a href="#">For Business</a><a href="#">Contact Us</a>
  </nav>
  <div class="footer-brand"><span class="mark"></span>Marwick Agency</div>
  <div class="footer-rule"></div>
  <p class="copyright">© Copyright information here</p>
</footer>

</body>
</html>
```